Packaging design for a revolutionary hi-protein snack of Norwegian salmon

We need a breathtaking packing design for a smal snack bag (30 g) for a revolutionary new hi-protein snack made of Norwegian salmon. The product will be made with two different flavors; MANGO and WASABI. The product is extreme high in protein (60%) and omega 3, and are just natural.

We want to see a bold and fresh design that appeals to protein lovers of all ages.

Target Market(s)

Our target market is boys and girls that are 18-35 years old and that are interested in working out and eating healthy.

Industry/Entity Type

Snack industry (functional food, healthy snack, protein snack)

Font styles to use
Sans Serif

Requirements
Must have
• The package design must give the customer a WOW feeling. "HI-PROTEIN SNACK" must be highligted. Further, the design must use the Four Factors setup (attached).

```html
<!DOCTYPE html>
<html lang="en">
<head>
<meta charset="UTF-8">
<title>Salto Protein Bites – Mango Flavor pack</title>
<link rel="stylesheet" href="https://fonts.googleapis.com/css2?family=Roboto+Condensed:wght@700&family=Lexend:wght@400&family=Bitter:wght@500&family=Arimo:ital,wght@1,700&display=swap">
<style>
  :root {
    --backdrop: #d9860f;
    --pack-light: #ffc24a;
    --pack-mid: #f5a623;
    --pack-dark: #e08a12;
    --crimp: #e39a2a;
    --red: #d9151c;
    --green: #1d7a1f;
    --dark-green: #1a6b1d;
    --white: #ffffff;
    --ink: #1a1a1a;
    --jerky-light: #f7a64a;
    --jerky-dark: #c24f12;
  }
  * { margin: 0; padding: 0; box-sizing: border-box; }
  html, body { width: 1200px; height: 933px; overflow: hidden; }
  body { background: var(--backdrop); position: relative; }

  .pack {
    position: absolute;
    left: 330px; top: 30px;
    width: 540px; height: 873px;
    background: radial-gradient(ellipse at 45% 35%, var(--pack-light) 0%, var(--pack-mid) 55%, var(--pack-dark) 100%);
    overflow: hidden;
  }
  .crimp {
    position: absolute; left: 0; right: 0;
    background: repeating-linear-gradient(180deg, var(--crimp) 0 3px, var(--pack-light) 3px 6px);
  }
  .crimp--top { top: 0; height: 80px; }
  .crimp--bottom { bottom: 0; height: 16px; }
  .hang-hole {
    position: absolute; left: 220px; top: 34px;
    width: 100px; height: 14px; border-radius: 7px;
    background: var(--backdrop);
  }

  .brand {
    position: absolute; left: 58px; top: 180px;
    font-family: "Roboto Condensed", sans-serif; font-weight: 700;
    font-size: 30px; line-height: 1; color: var(--ink);
  }

  .title {
    position: absolute; left: 0; right: 0; top: 236px;
    text-align: center;
    font-family: "Roboto Condensed", sans-serif; font-weight: 700;
    color: var(--red); line-height: 1;
  }
  .title__name { display: block; font-size: 112px; letter-spacing: 2px; }
  .title__sub { display: block; font-size: 50px; margin-top: 6px; letter-spacing: 1px; }

  .flavor {
    position: absolute; left: 0; right: 0; top: 462px;
    text-align: center;
    font-family: "Lexend", sans-serif; font-size: 50px; line-height: 1;
    color: var(--dark-green); word-spacing: 10px;
  }

  .product-photo {
    position: absolute; left: 110px; top: 560px;
    width: 320px; height: 220px;
    border-radius: 45% 50% 40% 45%;
    background: radial-gradient(ellipse at 50% 45%, var(--jerky-light) 0%, #e0752a 55%, var(--jerky-dark) 100%);
  }

  .claim {
    position: absolute; left: 0; top: 820px;
    width: 450px; height: 38px;
    background: var(--green);
    border-top: 3px solid var(--white);
    font-family: "Bitter", serif; font-weight: 500;
    font-size: 21px; color: var(--white);
    line-height: 35px; padding-left: 16px;
    white-space: nowrap;
  }
  .net-weight {
    position: absolute; left: 452px; top: 772px;
    width: 78px; height: 86px;
    background: var(--red);
    font-family: "Arimo", sans-serif; font-style: italic; font-weight: 700;
    text-align: center; color: var(--ink);
  }
  .net-weight__label { display: block; font-size: 10px; color: var(--white); padding-top: 14px; line-height: 1.4; }
  .net-weight__value { display: block; font-size: 26px; margin-top: 6px; }
</style>
</head>
<body>
  <main class="pack">
    <div class="crimp crimp--top"></div>
    <div class="hang-hole"></div>

    <div class="brand">Tidefin</div>

    <h1 class="title">
      <span class="title__name">SALTO</span>
      <span class="title__sub">PROTEIN BITES</span>
    </h1>

    <p class="flavor">Mango Flavor</p>

    <div class="product-photo" role="img" aria-label="Pile of mango-glazed salmon jerky pieces"></div>

    <p class="claim">PROTEIN (60%) AND OMEGA 3,</p>
    <div class="net-weight">
      <span class="net-weight__label">NET<br>WEIGHT</span>
      <span class="net-weight__value">30g</span>
    </div>

    <div class="crimp crimp--bottom"></div>
  </main>
</body>
</html>
```